design an app for runners to engage them in Pacewell Crew

Creative Brief: Running Application - Pacewell Crew
Objective
To design a simple yet impactful mobile application for runners, centered around Pacewell Crew. The app should offer an engaging, user-friendly experience while encouraging participation in running challenges. Starting with a minimalist and robust version, the design must focus on essential features, allowing for future enhancements as the user base grows.

Target Audience
Primary Users: Casual to dedicated runners who enjoy tracking their progress and participating in challenges.
Motivations: Community-driven goals, personal achievements, and tangible rewards.
Needs: A visually appealing, straightforward interface with real-time progress tracking and clear challenge objectives.
Core Features
Main Screen: Current Challenge

Displays the active challenge with a title, visual, prize description, and countdown for kilometers remaining.
Prominent “Join” button for easy participation.
Quick access to challenge conditions (eg, most kilometers, fastest pace, random draw).
Challenge Details

Includes challenge rules, detailed prize information, and victory conditions.
Simplified text for clarity and engagement.
Past Challenges

Showcases previous challenges, total kilometers achieved, and winners.
Admin Section

Enables challenge creation with scheduling, descriptions, and victory criteria.
Minimalist design for ease of use.
Look and Feel
Visual Identity: Clean, modern, and energetic design reflecting the spirit of running and collective achievement.
Color Palette:
Vibrant primary colors: Blue and green for energy and motivation.
Accent colors: Orange or yellow for highlights, paired with a dark background for strong contrast.
Typography:
Sans-serif fonts like Lato or Montserrat for readability.
Bold, prominent numbers for key statistics like kilometers completed.
Icons and Graphics:
Minimalistic icons with light, functional animations (eg, a moving kilometer counter).
Clear, motivational visuals to support collective progress.
Tone and Style
Tone: Encouraging, community-focused, and goal-oriented.
Style: Minimalistic with a focus on clarity and user engagement.
References
Inspirations:
Tavro Stride Circle for its simplicity and modern interface.
Pellux for its community features and tracking precision.
Deliverables
Wireframes and UI designs for all key screens: login, current challenge, challenge details, past challenges, and admin panel.
Visual assets: icons, buttons, and animations.
A consistent design system to ensure scalability for future features.
Updates

Target Market(s)

Casual to dedicated runners who enjoy tracking their progress and participating in challenges.

Industry/Entity Type

sport

Font styles to use
Sans Serif

Colors

Designer to choose colors to be used in the design.

Requirements
Must have
• to design all screens

```html
<!DOCTYPE html>
<html lang="en">
<head>
<meta charset="utf-8">
<title>Pacewell Crew – App Screens</title>
<link rel="stylesheet" href="https://fonts.googleapis.com/css2?family=Montserrat:wght@500;600;700;800&family=Open+Sans:wght@400;600;700&display=swap">
<style>
:root{
  --bg-a:#b9ad72;
  --bg-b:#ecc22a;
  --screen:#ffffff;
  --orange:#f7861f;
  --orange-bar:#f26a3b;
  --yellow:#f7b52b;
  --navy:#26235e;
  --ink:#2b2b2b;
  --muted:#6f6f6f;
  --faint:#b9b9b9;
  --field:#f3f3f3;
  --field-line:#e2e2e2;
  --ring-track:#d8d6ea;
  --nav:#f7f7f7;
  --icon:#9a9a9a;
}
*{box-sizing:border-box;margin:0;padding:0}
html,body{width:1200px;height:835px;overflow:hidden}
body{
  position:relative;
  background:linear-gradient(120deg,var(--bg-a) 0%,#c8b25c 45%,var(--bg-b) 100%);
  font-family:"Open Sans",sans-serif;color:var(--ink);
}
.screen{position:absolute;background:var(--screen);overflow:hidden;box-shadow:0 6px 18px rgba(0,0,0,.08)}
.screen > *{position:absolute}
.screen--signup{left:108px;top:177px;width:232px;height:505px;border-radius:22px}
.screen--week{left:446px;top:202px;width:188px;height:407px}
.screen--last{left:645px;top:286px;width:188px;height:418px}
.screen--profile{left:844px;top:206px;width:188px;height:408px}

.status-time{font-family:"Open Sans",sans-serif;font-weight:600;font-size:6.5px;color:var(--ink)}
.screen--signup .status-time{font-size:8.5px}
.status-icons{display:block}
.menu{width:12px;height:8px}

.brand{display:flex;align-items:center;gap:4px;white-space:nowrap}
.brand-dot{width:8px;height:8px;border-radius:50%;background:var(--orange);flex:none}
.brand-name{font-family:"Montserrat",sans-serif;font-weight:700;color:var(--navy);line-height:1}
.screen--signup .brand{left:0;width:232px;justify-content:center}
.screen--signup .brand-dot{width:16px;height:16px}
.screen--signup .brand-name{font-size:17px}
.brand--small .brand-name{font-size:8px}

.intro{left:0;width:232px;top:131px;text-align:center;font-size:6.3px;line-height:12.5px;color:var(--ink)}
.field{background:var(--field);border:1px solid var(--field-line);font-size:7.8px;color:var(--muted);padding-left:8px;display:flex;align-items:center;height:31px}
.field svg{position:absolute;right:8px;top:9px}
.btn{background:var(--orange);color:#fff;display:flex;align-items:center;justify-content:center;font-family:"Open Sans",sans-serif;font-weight:600}
.btn--join{left:17px;top:392px;width:197px;height:33px;font-size:10.5px}
.signin{left:0;width:232px;top:439px;text-align:center;font-size:7.5px;color:var(--ink)}
.signin span{color:var(--orange);font-weight:600}
.home-bar{left:77px;top:486px;width:78px;height:2px;border-radius:2px;background:#222}

.section-title{font-family:"Montserrat",sans-serif;font-weight:600;font-size:8px;letter-spacing:.3px;color:var(--ink);line-height:11.5px}
.see-all{font-size:5px;color:var(--muted);letter-spacing:.3px}
.day{width:20px;text-align:center;line-height:1}
.day b{display:block;font-size:7.5px;font-weight:600;color:var(--ink)}
.day small{display:block;font-size:5px;color:var(--muted);margin-top:3px}
.day--active{background:var(--orange);border-radius:3px;height:33px;width:25px;padding-top:8px}
.day--active b,.day--active small{color:#fff}
.metric-tabs{left:0;width:188px;top:115px;display:flex;justify-content:center;gap:4px;align-items:center;font-size:6.8px;font-weight:600}
.metric-tabs span{display:flex;align-items:center;gap:3px}
.stat{text-align:center;width:40px;line-height:1}
.stat b{display:block;font-family:"Montserrat",sans-serif;font-size:7.5px;font-weight:600;color:var(--orange)}
.stat small{display:block;font-size:5.3px;color:var(--ink);margin-top:3px}
.fine{font-size:4.3px;line-height:9.6px;color:var(--faint)}
.ring-label{text-align:center;line-height:1}
.ring-label b{display:block;font-family:"Montserrat",sans-serif;font-weight:500;font-size:11px;color:var(--orange)}
.ring-label small{display:block;font-size:6px;font-weight:600;color:var(--ink);margin-top:6px}
.btn--small{left:81px;top:200px;width:72px;height:21px;font-size:7.8px;font-weight:400}
.goal-title{font-size:6.2px;font-weight:600;color:var(--ink)}
.goal-km{font-family:"Montserrat",sans-serif;font-size:7.5px;font-weight:600;color:var(--navy)}
.week-dots{display:flex;gap:4.6px}
.week-dots div{width:10.4px;text-align:center;font-size:3.8px;color:var(--ink)}
.week-dots svg{display:block;margin-bottom:2px}
.btn--wide{left:15px;width:163px;height:28px;font-size:8.5px;font-weight:400}
.tabbar{left:0;width:188px;height:35px;background:var(--nav);display:flex;justify-content:space-around;align-items:center;padding:0 10px}

.card{background:#fff;box-shadow:0 1px 5px rgba(0,0,0,.08)}
.axis-y{font-size:4.3px;color:var(--muted);text-align:right;width:12px}
.axis-x{font-size:5px;color:var(--muted);width:16px;text-align:center}
.bar{width:2.4px;background:var(--orange-bar)}
.grid-line{height:1px;background:#f1f1f1}
.mini-head{display:flex;align-items:center;gap:3px;font-size:4.4px;color:var(--ink)}
.mini-val{font-size:5.3px;color:var(--ink)}

.avatar{border-radius:50%;background:radial-gradient(circle at 50% 40%,#c98f72 0%,#7a3a2e 60%,#3a1c18 100%)}
.person{font-size:6.5px;font-weight:600;color:var(--ink)}
.place{font-size:5.2px;color:var(--ink)}
.prize-card{left:17px;top:161px;width:48px;height:51px;display:flex;flex-direction:column;align-items:center;justify-content:center;gap:5px;font-size:4.2px;color:var(--ink)}
.legend{display:flex;align-items:center;gap:5px;font-size:4.4px;color:var(--ink)}
.legend i{display:block;width:9px;height:2px}
.gauge-label{font-size:3.8px;color:var(--ink);text-align:center;width:20px}
</style>
</head>
<body>

<!-- Sign up -->
<section class="screen screen--signup" aria-label="Sign up screen">
  <span class="status-time" style="left:23px;top:7px">9:41</span>
  <svg class="status-icons" style="left:180px;top:10px" width="40" height="8" viewBox="0 0 40 8" aria-hidden="true">
    <rect x="0" y="5" width="1.6" height="3" fill="#222"/><rect x="2.4" y="3.6" width="1.6" height="4.4" fill="#222"/><rect x="4.8" y="2.2" width="1.6" height="5.8" fill="#222"/><rect x="7.2" y="0.6" width="1.6" height="7.4" fill="#222"/>
    <path d="M12 3.2a6 6 0 0 1 8 0M13.5 4.8a3.6 3.6 0 0 1 5 0" stroke="#222" stroke-width="1.1" fill="none"/><circle cx="16" cy="6.6" r="1" fill="#222"/>
    <rect x="25" y="1" width="12" height="6" rx="1.4" fill="none" stroke="#999" stroke-width=".6"/><rect x="26" y="2" width="10" height="4" rx=".8" fill="#222"/><rect x="37.5" y="3" width="1" height="2" fill="#999"/>
  </svg>
  <div class="brand" style="top:64px"><span class="brand-dot"></span><span class="brand-name">Pacewell Crew</span></div>
  <p class="intro">Lorem ipsum dolor sit amet, consectetur adipiscing elit.<br>Neque gravida. Auctor massa ipsum ac augue.</p>
  <div class="field" style="left:17px;top:173px;width:92px">First Name</div>
  <div class="field" style="left:122px;top:173px;width:92px">Last Name</div>
  <div class="field" style="left:17px;top:215px;width:197px">Email address</div>
  <div class="field" style="left:17px;top:258px;width:197px">Password
    <svg width="14" height="12" viewBox="0 0 14 12" aria-hidden="true"><path d="M1 6c2-3 4-4 6-4s4 1 6 4c-2 3-4 4-6 4S3 9 1 6z" fill="none" stroke="#aaa" stroke-width="1"/><circle cx="7" cy="6" r="2" fill="none" stroke="#aaa" stroke-width="1"/><path d="M2 11L12 1" stroke="#aaa" stroke-width="1"/></svg>
  </div>
  <div class="field" style="left:17px;top:300px;width:197px">Address</div>
  <div class="field" style="left:17px;top:343px;width:105px">City</div>
  <div class="field" style="left:135px;top:343px;width:79px">Area Code</div>
  <div class="btn btn--join">Join Us</div>
  <p class="signin">Have an account? <span>Sign In</span></p>
  <div class="home-bar"></div>
</section>

<!-- This week's challenge -->
<section class="screen screen--week" aria-label="This week's challenge screen">
  <span class="status-time" style="left:9px;top:7px">9:41</span>
  <svg class="status-icons" style="left:147px;top:8px" width="34" height="7" viewBox="0 0 40 8" aria-hidden="true">
    <rect x="0" y="5" width="1.6" height="3" fill="#222"/><rect x="2.4" y="3.6" width="1.6" height="4.4" fill="#222"/><rect x="4.8" y="2.2" width="1.6" height="5.8" fill="#222"/><rect x="7.2" y="0.6" width="1.6" height="7.4" fill="#222"/>
    <path d="M12 3.2a6 6 0 0 1 8 0M13.5 4.8a3.6 3.6 0 0 1 5 0" stroke="#222" stroke-width="1.1" fill="none"/><circle cx="16" cy="6.6" r="1" fill="#222"/>
    <rect x="25" y="1" width="12" height="6" rx="1.4" fill="none" stroke="#999" stroke-width=".6"/><rect x="26" y="2" width="10" height="4" rx=".8" fill="#222"/>
  </svg>
  <svg class="menu" style="left:7px;top:29px" viewBox="0 0 12 8" aria-hidden="true"><path d="M0 .5h12M0 4h12M0 7.5h12" stroke="#333" stroke-width=".9"/></svg>
  <div class="brand brand--small" style="left:67px;top:29px"><span class="brand-dot"></span><span class="brand-name">Pacewell Crew</span></div>
  <h2 class="section-title" style="left:7px;top:51px">This Week’s Challenge</h2>
  <span class="see-all" style="left:161px;top:54px">See All</span>

  <div class="day" style="left:2px;top:81px"><b>12</b><small>Mo</small></div>
  <div class="day" style="left:25px;top:81px"><b>13</b><small>Tu</small></div>
  <div class="day" style="left:50px;top:81px"><b>14</b><small>Wed</small></div>
  <div class="day day--active" style="left:72px;top:72px"><b>15</b><small>Th</small></div>
  <div class="day" style="left:97px;top:81px"><b>16</b><small>Fr</small></div>
  <div class="day" style="left:120px;top:81px"><b>17</b><small>Sa</small></div>
  <div class="day" style="left:142px;top:81px"><b>18</b><small>Su</small></div>
  <div class="day" style="left:166px;top:81px"><b>19</b><small>Mo</small></div>

  <div class="metric-tabs">
    <span><svg width="8" height="7" viewBox="0 0 8 7" aria-hidden="true"><path d="M4 6.5L1 3.6A1.7 1.7 0 0 1 4 1.4a1.7 1.7 0 0 1 3 2.2z" fill="none" stroke="#f7861f" stroke-width=".9"/></svg>Cardio Points</span>
    <span><svg width="7" height="8" viewBox="0 0 7 8" aria-hidden="true"><circle cx="4.6" cy="1.2" r=".9" fill="#f7861f"/><path d="M4 2.6L2.6 4.4l1.6 1-1 2.4M3.2 3.4l-2 .4M4.2 3.6l1.6 1" stroke="#f7861f" stroke-width=".7" fill="none"/></svg>Steps</span>
  </div>
  <div class="stat" style="left:45px;top:137px"><b>1.000</b><small>Calories</small></div>
  <div class="stat" style="left:78px;top:137px"><b>3.83</b><small>Km</small></div>
  <div class="stat" style="left:110px;top:137px"><b>70</b><small>Move Min</small></div>
  <p class="fine" style="left:16px;top:160px;width:158px">Run together with your crew this week and push the shared total higher. Every step counts toward the group goal and weekly rewards.</p>

  <svg style="left:7px;top:194px" width="62" height="62" viewBox="0 0 62 62" aria-hidden="true">
    <circle cx="31" cy="31" r="28" fill="none" stroke="var(--ring-track)" stroke-width="2.6"/>
    <circle cx="31" cy="31" r="28" fill="none" stroke="var(--orange)" stroke-width="2.6" stroke-dasharray="145 176" transform="rotate(-20 31 31)" stroke-linecap="round"/>
  </svg>
  <div class="ring-label" style="left:13px;top:213px;width:50px"><b>1264</b><small>Km</small></div>
  <div class="btn btn--small">Join Challenge</div>
  <p class="fine" style="left:78px;top:229px;width:102px">Sign up before Sunday to add your distance to the team count and unlock a chance at this week's prize draw.</p>
  <svg style="left:159px;top:272px" width="5" height="7" viewBox="0 0 5 7" aria-hidden="true"><path d="M1 1l2.5 2.5L1 6" stroke="#777" stroke-width=".8" fill="none"/></svg>
  <span class="goal-title" style="left:12px;top:282px">Your goals for Next Week</span>
  <span class="goal-km" style="left:13px;top:306px">5 Km</span>
  <div class="week-dots" style="left:68px;top:300px">
    <div><svg width="10" height="10" viewBox="0 0 10 10"><circle cx="5" cy="5" r="4" fill="none" stroke="var(--navy)" stroke-width="1"/><circle cx="5" cy="5" r="2.6" fill="none" stroke="var(--orange)" stroke-width="1"/></svg>S</div>
    <div><svg width="10" height="10" viewBox="0 0 10 10"><circle cx="5" cy="5" r="4" fill="none" stroke="var(--navy)" stroke-width="1"/><circle cx="5" cy="5" r="2.6" fill="none" stroke="var(--orange)" stroke-width="1"/></svg>M</div>
    <div><svg width="10" height="10" viewBox="0 0 10 10"><circle cx="5" cy="5" r="4" fill="none" stroke="var(--navy)" stroke-width="1"/><circle cx="5" cy="5" r="2.6" fill="none" stroke="var(--orange)" stroke-width="1"/></svg>T</div>
    <div><svg width="10" height="10" viewBox="0 0 10 10"><circle cx="5" cy="5" r="4" fill="none" stroke="var(--navy)" stroke-width="1"/><circle cx="5" cy="5" r="2.6" fill="none" stroke="var(--orange)" stroke-width="1"/></svg>W</div>
    <div><svg width="10" height="10" viewBox="0 0 10 10"><circle cx="5" cy="5" r="4" fill="none" stroke="var(--navy)" stroke-width="1"/><circle cx="5" cy="5" r="2.6" fill="none" stroke="var(--orange)" stroke-width="1"/></svg>T</div>
    <div><svg width="10" height="10" viewBox="0 0 10 10"><circle cx="5" cy="5" r="4" fill="none" stroke="var(--navy)" stroke-width="1"/><circle cx="5" cy="5" r="2.6" fill="none" stroke="var(--orange)" stroke-width="1"/></svg>F</div>
    <div><svg width="10" height="10" viewBox="0 0 10 10"><circle cx="5" cy="5" r="4" fill="none" stroke="var(--navy)" stroke-width="1"/><circle cx="5" cy="5" r="2.6" fill="none" stroke="var(--orange)" stroke-width="1"/></svg>S</div>
  </div>
  <div class="btn btn--wide" style="top:344px">Next&nbsp; Challenge</div>
  <nav class="tabbar" style="top:373px" aria-label="Main navigation">
    <svg width="12" height="12" viewBox="0 0 12 12"><path d="M1.5 6L6 1.8 10.5 6M2.8 5v5.5h2.4V8h1.6v2.5h2.4V5" fill="none" stroke="var(--icon)" stroke-width=".9"/></svg>
    <svg width="12" height="12" viewBox="0 0 12 12"><circle cx="7.6" cy="1.8" r="1.2" fill="none" stroke="var(--orange)" stroke-width=".9"/><path d="M6.6 3.8L4.4 6.4l2.4 1.6-1.4 3.4M5.4 4.6l-2.8.6M7 5l2.2 1.4M4.4 6.4L2.2 9" fill="none" stroke="var(--orange)" stroke-width=".9"/></svg>
    <svg width="14" height="12" viewBox="0 0 14 12"><path d="M1 11l4-4 3 2 5-6M10 3h3v3" fill="none" stroke="var(--icon)" stroke-width=".9"/><path d="M2 11V9M5 11V8M8 11V9.6M11 11V6" stroke="var(--icon)" stroke-width=".7"/></svg>
    <svg width="12" height="12" viewBox="0 0 12 12"><circle cx="6" cy="3.6" r="2.4" fill="none" stroke="var(--icon)" stroke-width=".9"/><path d="M1.6 11.4a4.4 4.4 0 0 1 8.8 0z" fill="none" stroke="var(--icon)" stroke-width=".9"/></svg>
  </nav>
</section>

<!-- Last week's challenge -->
<section class="screen screen--last" aria-label="Last week's challenge screen">
  <span class="status-time" style="left:8px;top:7px">9:41</span>
  <svg class="status-icons" style="left:147px;top:8px" width="34" height="7" viewBox="0 0 40 8" aria-hidden="true">
    <rect x="0" y="5" width="1.6" height="3" fill="#222"/><rect x="2.4" y="3.6" width="1.6" height="4.4" fill="#222"/><rect x="4.8" y="2.2" width="1.6" height="5.8" fill="#222"/><rect x="7.2" y="0.6" width="1.6" height="7.4" fill="#222"/>
    <path d="M12 3.2a6 6 0 0 1 8 0M13.5 4.8a3.6 3.6 0 0 1 5 0" stroke="#222" stroke-width="1.1" fill="none"/><circle cx="16" cy="6.6" r="1" fill="#222"/>
    <rect x="25" y="1" width="12" height="6" rx="1.4" fill="none" stroke="#999" stroke-width=".6"/><rect x="26" y="2" width="10" height="4" rx=".8" fill="#222"/>
  </svg>
  <svg class="menu" style="left:7px;top:29px" viewBox="0 0 12 8" aria-hidden="true"><path d="M0 .5h12M0 4h12M0 7.5h12" stroke="#333" stroke-width=".9"/></svg>
  <div class="brand brand--small" style="left:66px;top:30px"><span class="brand-dot"></span><span class="brand-name">Pacewell Crew</span></div>
  <h2 class="section-title" style="left:7px;top:51px">Last Week Challenge</h2>

  <div class="card" style="left:14px;top:66px;width:164px;height:117px"></div>
  <span class="axis-y" style="left:12px;top:79px">1k</span>
  <span class="axis-y" style="left:17px;top:93px">500</span>
  <span class="axis-y" style="left:17px;top:107px">200</span>
  <span class="axis-y" style="left:17px;top:122px">100</span>
  <span class="axis-y" style="left:16px;top:136px">50</span>
  <span class="axis-y" style="left:15px;top:150px">0</span>
  <div class="grid-line" style="left:33px;top:82px;width:138px"></div>
  <div class="grid-line" style="left:33px;top:96px;width:138px"></div>
  <div class="grid-line" style="left:33px;top:110px;width:138px"></div>
  <div class="grid-line" style="left:33px;top:125px;width:138px"></div>
  <div class="grid-line" style="left:33px;top:139px;width:138px"></div>
  <div class="bar" style="left:38px;top:124px;height:29px"></div>
  <div class="bar" style="left:60px;top:96px;height:57px"></div>
  <div class="bar" style="left:78px;top:116px;height:37px"></div>
  <div class="bar" style="left:100px;top:130px;height:23px"></div>
  <div class="bar" style="left:119px;top:88px;height:65px"></div>
  <div class="bar" style="left:140px;top:110px;height:43px"></div>
  <div class="bar" style="left:160px;top:105px;height:48px"></div>
  <span class="axis-x" style="left:31px;top:163px">Su</span>
  <span class="axis-x" style="left:53px;top:163px">Mo</span>
  <span class="axis-x" style="left:71px;top:163px">Tu</span>
  <span class="axis-x" style="left:93px;top:163px">We</span>
  <span class="axis-x" style="left:112px;top:163px">Th</span>
  <span class="axis-x" style="left:133px;top:163px">Fr</span>
  <span class="axis-x" style="left:153px;top:163px">Sa</span>
  <p class="fine" style="left:15px;top:187px;width:160px">Last week the community logged strong distances every day. See how each run added up and who finished on top of the board.</p>
  <h2 class="section-title" style="left:14px;top:218px">On Going<br>Challenge</h2>

  <div class="card" style="left:12px;top:239px;width:163px;height:60px"></div>
  <div class="mini-head" style="left:17px;top:259px"><svg width="6" height="6" viewBox="0 0 12 12"><circle cx="7.6" cy="1.8" r="1.4" fill="var(--orange-bar)"/><path d="M6.6 3.8L4.4 6.4l2.4 1.6-1.4 3.4M5.4 4.6l-2.8.6M7 5l2.2 1.4" fill="none" stroke="var(--orange-bar)" stroke-width="1.4"/></svg>Distance Total</div>
  <div class="mini-head" style="left:77px;top:259px"><svg width="6" height="6" viewBox="0 0 6 6"><circle cx="3" cy="3" r="2.5" fill="none" stroke="var(--orange-bar)" stroke-width=".7"/><path d="M3 1.6V3h1.2" stroke="var(--orange-bar)" stroke-width=".7" fill="none"/></svg>Average Speed</div>
  <div class="mini-head" style="left:139px;top:259px"><svg width="6" height="6" viewBox="0 0 6 6"><path d="M3 .6C4.6 2 5 3 5 4a2 2 0 0 1-4 0c0-1 .6-1.6 1-2 .2.8.6 1 1 1z" fill="none" stroke="var(--orange-bar)" stroke-width=".7"/></svg>Fastest Km</div>
  <span class="mini-val" style="left:18px;top:272px">400 km</span>
  <span class="mini-val" style="left:77px;top:272px">8k hours</span>
  <span class="mini-val" style="left:138px;top:272px">12.5 km/hr</span>
  <p class="fine" style="left:15px;top:309px;width:160px">Keep your pace steady to stay in the running. Totals update after every synced activity so you always know where the group stands.</p>
  <div class="btn btn--wide" style="left:14px;top:344px;width:164px">Result</div>
  <nav class="tabbar" style="top:384px" aria-label="Main navigation">
    <svg width="12" height="12" viewBox="0 0 12 12"><path d="M1.5 6L6 1.8 10.5 6M2.8 5v5.5h2.4V8h1.6v2.5h2.4V5" fill="none" stroke="var(--icon)" stroke-width=".9"/></svg>
    <svg width="12" height="12" viewBox="0 0 12 12"><circle cx="7.6" cy="1.8" r="1.2" fill="none" stroke="var(--icon)" stroke-width=".9"/><path d="M6.6 3.8L4.4 6.4l2.4 1.6-1.4 3.4M5.4 4.6l-2.8.6M7 5l2.2 1.4M4.4 6.4L2.2 9" fill="none" stroke="var(--icon)" stroke-width=".9"/></svg>
    <svg width="14" height="12" viewBox="0 0 14 12"><path d="M1 11l4-4 3 2 5-6M10 3h3v3" fill="none" stroke="var(--orange)" stroke-width=".9"/><path d="M2 11V9M5 11V8M8 11V9.6M11 11V6" stroke="var(--orange)" stroke-width=".7"/></svg>
    <svg width="12" height="12" viewBox="0 0 12 12"><circle cx="6" cy="3.6" r="2.4" fill="none" stroke="var(--icon)" stroke-width=".9"/><path d="M1.6 11.4a4.4 4.4 0 0 1 8.8 0z" fill="none" stroke="var(--icon)" stroke-width=".9"/></svg>
  </nav>
</section>

<!-- Profile / prize -->
<section class="screen screen--profile" aria-label="Profile and prize screen">
  <span class="status-time" style="left:9px;top:7px">9:41</span>
  <svg class="status-icons" style="left:147px;top:8px" width="34" height="7" viewBox="0 0 40 8" aria-hidden="true">
    <rect x="0" y="5" width="1.6" height="3" fill="#222"/><rect x="2.4" y="3.6" width="1.6" height="4.4" fill="#222"/><rect x="4.8" y="2.2" width="1.6" height="5.8" fill="#222"/><rect x="7.2" y="0.6" width="1.6" height="7.4" fill="#222"/>
    <path d="M12 3.2a6 6 0 0 1 8 0M13.5 4.8a3.6 3.6 0 0 1 5 0" stroke="#222" stroke-width="1.1" fill="none"/><circle cx="16" cy="6.6" r="1" fill="#222"/>
    <rect x="25" y="1" width="12" height="6" rx="1.4" fill="none" stroke="#999" stroke-width=".6"/><rect x="26" y="2" width="10" height="4" rx=".8" fill="#222"/>
  </svg>
  <svg class="menu" style="left:7px;top:29px" viewBox="0 0 12 8" aria-hidden="true"><path d="M0 .5h12M0 4h12M0 7.5h12" stroke="#333" stroke-width=".9"/></svg>
  <div class="brand brand--small" style="left:68px;top:35px"><span class="brand-dot"></span><span class="brand-name">Pacewell Crew</span></div>
  <div class="avatar" role="img" aria-label="Profile photo of the runner" style="left:142px;top:43px;width:38px;height:38px"></div>
  <span class="person" style="left:11px;top:56px">Mara Ellison</span>
  <span class="place" style="left:11px;top:71px">Lakeview, USA</span>
  <p class="fine" style="left:11px;top:84px;width:96px">Weekend trail runner and early morning regular. Chasing a new half marathon best this season with the crew.</p>
  <h2 class="section-title" style="left:8px;top:143px">Priz<br>e</h2>
  <div class="card prize-card">
    <svg width="15" height="11" viewBox="0 0 15 11" aria-hidden="true"><path d="M1 2l3.2 3.6L7.5 1l3.3 4.6L14 2l-1.4 6.4H2.4z" fill="var(--yellow)"/><rect x="2.4" y="9" width="10.2" height="1.6" fill="var(--yellow)"/></svg>
    <span>FirstPrize</span>
  </div>
  <p class="fine" style="left:78px;top:164px;width:96px">Top distance earns the first prize. Finish the month with the most kilometres logged to claim it.</p>
  <h2 class="section-title" style="left:14px;top:213px">Here to<br>Win</h2>
  <div class="card" style="left:14px;top:238px;width:163px;height:61px"></div>
  <span class="place" style="left:21px;top:248px">Total Km</span>
  <div class="legend" style="left:21px;top:262px"><i style="background:var(--orange-bar)"></i>Average Speed</div>
  <div class="legend" style="left:21px;top:274px"><i style="background:var(--yellow)"></i>Fastest Km</div>
  <svg style="left:72px;top:260px" width="22" height="22" viewBox="0 0 22 22" aria-hidden="true"><circle cx="11" cy="11" r="9.5" fill="none" stroke="#eee" stroke-width="1.6"/><circle cx="11" cy="11" r="9.5" fill="none" stroke="var(--orange-bar)" stroke-width="1.6" stroke-dasharray="48 60" transform="rotate(-90 11 11)"/></svg>
  <span class="gauge-label" style="left:73px;top:269px">80%</span>
  <svg style="left:110px;top:260px" width="22" height="22" viewBox="0 0 22 22" aria-hidden="true"><circle cx="11" cy="11" r="9.5" fill="none" stroke="#eee" stroke-width="1.6"/><circle cx="11" cy="11" r="9.5" fill="none" stroke="var(--yellow)" stroke-width="1.6" stroke-dasharray="40 60" transform="rotate(-90 11 11)"/></svg>
  <span class="gauge-label" style="left:111px;top:269px">Km/hr</span>
  <p class="fine" style="left:14px;top:309px;width:162px">Each kilometre you log brings the countdown closer to zero. Join now and help the group reach the finish line together.</p>
  <div class="btn btn--wide" style="left:14px;top:344px;width:164px">Km countdown Join</div>
  <nav class="tabbar" style="top:373px" aria-label="Main navigation">
    <svg width="12" height="12" viewBox="0 0 12 12"><path d="M1.5 6L6 1.8 10.5 6M2.8 5v5.5h2.4V8h1.6v2.5h2.4V5" fill="none" stroke="var(--icon)" stroke-width=".9"/></svg>
    <svg width="12" height="12" viewBox="0 0 12 12"><circle cx="7.6" cy="1.8" r="1.2" fill="none" stroke="var(--icon)" stroke-width=".9"/><path d="M6.6 3.8L4.4 6.4l2.4 1.6-1.4 3.4M5.4 4.6l-2.8.6M7 5l2.2 1.4M4.4 6.4L2.2 9" fill="none" stroke="var(--icon)" stroke-width=".9"/></svg>
    <svg width="14" height="12" viewBox="0 0 14 12"><path d="M1 11l4-4 3 2 5-6M10 3h3v3" fill="none" stroke="var(--icon)" stroke-width=".9"/><path d="M2 11V9M5 11V8M8 11V9.6M11 11V6" stroke="var(--icon)" stroke-width=".7"/></svg>
    <svg width="12" height="12" viewBox="0 0 12 12"><circle cx="6" cy="3.6" r="2.4" fill="none" stroke="var(--orange)" stroke-width=".9"/><path d="M1.6 11.4a4.4 4.4 0 0 1 8.8 0z" fill="none" stroke="var(--orange)" stroke-width=".9"/></svg>
  </nav>
</section>

</body>
</html>
```